Book cover design for modern bagpipe music book

This music book will be A4 in size and requires a design for the front and back cover. The focus is on creating a modern and eye catching design, breaking away from the stereotypes of what people think of when they think of bagpipes. Think the OPPOSITE of a bagpiper in a full kilt standing on top of a mountain playing Copper Lanterns Rising!

Book title: Rise Hum March Rest

Other front cover text : Music for the bagpipes by Dermot Fairley

Front cover file ideas uploaded

2 pictures of bagpipes attached.

- The real set of bagpipes give an idea of the correct finer details

- The toy bagpipes perhaps have a better shape with the left 'stick' down

Back cover - No real brief. Keen for it not to be a full block single colour though.

Design requires 3mm bleed for print

Open to ideas and suggestions! Thank you!

```html
<!DOCTYPE html>
<html lang="en">
<head>
<meta charset="utf-8">
<title>Rise Hum March Rest — Cover Spread</title>
<link rel="stylesheet" href="https://fonts.googleapis.com/css2?family=Bebas+Neue&family=Oswald:wght@300;500&family=EB+Garamond&display=swap">
<style>
  :root {
    --page: #f2f2f2;
    --ink: #050505;
    --white: #ffffff;
    --teal: #2f8f8f;
    --violet: #7a2a86;
    --magenta: #d4145a;
    --crimson: #ee2a4a;
    --orange: #f5641e;
  }
  * { margin: 0; padding: 0; box-sizing: border-box; }
  html, body { width: 899px; height: 1200px; overflow: hidden; background: var(--page); }
  .canvas { position: relative; width: 899px; height: 1200px; }

  .spread {
    position: absolute; left: 20px; top: 302px;
    width: 860px; height: 596px;
    background: var(--ink);
    display: flex;
    box-shadow: 0 2px 8px rgba(0,0,0,.25);
    overflow: hidden;
  }

  /* Back cover */
  .back-cover { position: relative; width: 399px; height: 100%; }
  .back-art {
    position: absolute; inset: 0;
    background:
      radial-gradient(ellipse 45% 22% at 55% 6%, rgba(47,143,143,.8), transparent 70%),
      radial-gradient(ellipse 35% 20% at 15% 10%, rgba(122,42,134,.7), transparent 70%),
      radial-gradient(ellipse 70% 40% at 30% 55%, rgba(212,20,90,.85), transparent 70%),
      radial-gradient(ellipse 60% 35% at 20% 85%, rgba(245,100,30,.85), transparent 70%),
      radial-gradient(ellipse 50% 35% at 75% 60%, rgba(238,42,74,.55), transparent 70%);
  }
  .blurb {
    position: absolute; left: 36px; top: 52px; width: 340px;
    font-family: "EB Garamond", serif; font-size: 9.2px; line-height: 1.32;
    color: var(--white); text-align: justify; hyphens: auto;
  }
  .isbn-box {
    position: absolute; left: 40px; bottom: 48px;
    width: 102px; height: 57px; background: var(--white);
  }

  /* Spine */
  .spine { position: relative; width: 64px; height: 100%; }
  .spine-title {
    position: absolute; left: 50%; top: 32px;
    transform: translateX(-50%) rotate(180deg);
    writing-mode: vertical-rl;
    font-family: "Bebas Neue", sans-serif; font-size: 33px; letter-spacing: .5px;
    color: var(--white); white-space: nowrap;
  }
  .spine-author {
    position: absolute; left: 50%; bottom: 56px;
    transform: translateX(-50%) rotate(180deg);
    writing-mode: vertical-rl;
    font-family: "Oswald", sans-serif; font-weight: 300; font-size: 10px; letter-spacing: 3px;
    color: var(--white); white-space: nowrap;
  }

  /* Front cover */
  .front-cover { position: relative; width: 397px; height: 100%; }
  .front-art {
    position: absolute; inset: 0;
    background:
      radial-gradient(ellipse 20% 10% at 62% 18%, rgba(245,100,30,.95), transparent 75%),
      radial-gradient(ellipse 18% 28% at 45% 42%, rgba(238,42,74,.9), transparent 75%),
      radial-gradient(ellipse 25% 22% at 60% 62%, rgba(212,20,90,.85), transparent 75%),
      radial-gradient(ellipse 25% 18% at 70% 80%, rgba(122,42,134,.8), transparent 75%),
      radial-gradient(ellipse 20% 12% at 55% 90%, rgba(47,143,143,.55), transparent 75%);
  }
  .front-author {
    position: absolute; right: 32px; top: 56px;
    font-family: "Oswald", sans-serif; font-weight: 300; font-size: 13px; letter-spacing: 4px;
    color: var(--white);
  }
  .front-title {
    position: absolute; left: 10px; top: 48px;
    font-family: "Bebas Neue", sans-serif; font-size: 160px; line-height: 133px;
    color: var(--white);
  }
  .front-title span { display: block; }
  .front-subtitle {
    position: absolute; right: 20px; top: 320px;
    writing-mode: vertical-rl;
    font-family: "Oswald", sans-serif; font-weight: 300; font-size: 11px; letter-spacing: 4px;
    color: var(--white); white-space: nowrap;
  }
</style>
</head>
<body>
<main class="canvas">
  <section class="spread">
    <article class="back-cover">
      <div class="back-art" role="img" aria-label="Woodcut-style illustration of a piper's hand and bag in teal, magenta, red and orange"></div>
      <p class="blurb">Lorem ipsum dolor sit amet, consectetur adipiscing elit. Maecenas eu malesuada purus. Lorem ipsum dolor sit amet, consectetur adipiscing elit. Phasellus quis leo ut justo viverra vestibulum at in elit. Vestibulum vestibulum a magna vitae molestie. Phasellus consectetur ultrices quam, sit amet suscipit libero sollicitudin ac. Cras quis commodo est, vitae ullamcorper neque. Nullam sollicitudin fringilla risus, eu pretium ipsum volutpat quis. Integer id dui malesuada, accumsan massa imperdiet, auctor nisi. Proin consectetur ante aliquam est commodo, eu ullamcorper justo sagittis. Sed tincidunt, nulla ut mollis scelerisque, neque risus blandit sapien, non gravida augue tortor ut justo. Duis at dignissim nulla. Donec convallis, mauris aliquam scelerisque sodales, nisi ex malesuada lorem, id volutpat nulla orci id metus. Mauris euismod, nulla vitae convallis facilisis, lectus augue euismod mauris, vel faucibus orci lectus sed orci.</p>
      <div class="isbn-box"></div>
    </article>

    <aside class="spine">
      <h2 class="spine-title">RISE HUM MARCH REST</h2>
      <p class="spine-author">AUTHOR NAME</p>
    </aside>

    <article class="front-cover">
      <div class="front-art" role="img" aria-label="Illustrated set of bagpipes angled across the title, fading from orange through magenta to violet"></div>
      <p class="front-author">AUTHOR NAME</p>
      <h1 class="front-title"><span>RISE</span><span>HUM</span><span>MARCH</span><span>REST</span></h1>
      <p class="front-subtitle">MUSIC FOR THE BAGPIPES</p>
    </article>
  </section>
</main>
</body>
</html>
```